Website Redesign for a faith-based, not-for-profit health and human services organization

New website design for the Hearthside Faith Outreach House.
- Current site: www.hfohtr.org -
We are looking for a nice clean, simple, friendly-yet-elegant website layout.
Colors are #f5eed5 (cream), #FFFFFF (white), and all logo colors.
Design a layout for home page
Design a layout for general layouts
-layout only no html needed (preferably a high res PSD file format) -
Main menu should be along top with side navigation for submenu, no side menu on home page.
Also would be open to seeing some updated colors on the logo design, currently the colors are slightly outdated. The Vine of Plenty quilt design fits the organization’s mission and the rural farming / Amish-Mennonite-Brethren community around us.

ADDITIONAL PAGES AND MENU STRUCTURE ON NEW SITE

- How to Help
... Volunteer
... Donate Time
... Donate Money
... Donate Supplies
... Current Needs

- Programs

- News & Events
... Upcoming Events
... Upcoming Fundraisers
... Newsletter

- Our Partners

- About Us
... Overview
... Mission
... Staff Directory
... Board of Directors
... Annual Reports

- Contact

Our annual special event is Gather at the Hearth and should be integrated into the home page - see attached logos and banner

Websites with elements we like (from organizations doing similar work), each for a different reason....

1. http://www.kinbridgeway.org
Good design, color, clarity on this site. Multi-dimensional, photos...easy interaction, etc.

2. http://endfamineplainly.org
Quite simple, nothing fancy, but some good basic stuff here, and pretty easy to navigate...

3. http://www.neighborhub.org
Intrigued by the bulletin board design and the way they have their programs broken down to show impact, needs, etc. It has a lot of good information, but is really too verbose, some of the print is too small, etc. Not perfect, but some interesting design elements.

4. http://sharedlarder.org
Site is boring and not very well designed, but it has some of the features that we would like to see at the top, donations, partners, etc.

5. http://www.meadowlarkgrocers.org
Too many listings on the sidebar - needs to be cleaner & simpler, but a lot of good information and we like the way they show volunteer photos on the Our Helpers Shine Bright page...

About
Hearthside Faith Outreach House ("HFOH" or “the Center”) is a faith-based non-for-profit health and human services organization that exists as an outreach of and for the Ostrel Valley Unified School District.
Tagline: Mercy at Work (we work to serve the needs of the ‘least of these’ with compassion).

Mission
Our mission is to see lives transformed and the community enhanced by encouraging the oppressed, defending the cause of the weak and maintaining the rights of the poor - bringing together the resources of a caring community as a demonstration of the good news of Christ.

Company Overview
Hearthside Faith Outreach House works closely with the community in which it serves. A tremendous value is placed upon the partnerships that have formed with caring people within the community and with organizations that share the goal of bringing together resources to help those who need it most. Individuals, volunteers, churches, corporations, foundations, and government sources all pull together to help make our mission possible.

Since 1996 the Hearthside Faith Outreach House has collaboratively worked to see our community enhanced, adapting programs and services to meet the changing needs of the community.

Target Market(s)

people needing assistance in local community

Industry/Entity Type

Government

Requirements
Must have
• Good social button integration
Should not have
• No Find Us page like old website it is not needed

```html
<!DOCTYPE html>
<html lang="en">
<head>
<meta charset="utf-8">
<title>Hearthside Faith Outreach House</title>
<link href="https://fonts.googleapis.com/css2?family=Open+Sans:wght@400;600;700&display=swap" rel="stylesheet">
<style>
:root{
  --page:#f3f6fb;
  --maroon:#8d1b33;
  --maroon-light:#b8304d;
  --maroon-dark:#701026;
  --gold:#d9b44a;
  --gold-dark:#b8922e;
  --ink:#3a3a3a;
  --muted:#7d7d7d;
  --panel:#333333;
  --footer:#343434;
  --footer-text:#bdbdbd;
  --white:#ffffff;
}
*{box-sizing:border-box;margin:0;padding:0}
html,body{width:1167px;height:1200px;overflow:hidden;background:var(--page)}
body{font-family:'Open Sans',Arial,sans-serif;color:var(--ink)}
.page{position:relative;width:1167px;height:1200px;overflow:hidden}
.abs{position:absolute}

.brand{left:51px;top:40px;display:flex;align-items:center;gap:14px}
.brand-mark{width:58px;height:58px;background:var(--maroon)}
.brand-name{width:170px;font-size:20px;line-height:23px;font-weight:600;color:var(--maroon)}

.social{right:40px;top:32px;display:flex;align-items:center;gap:6px}
.social-label{font-size:11px;font-weight:700;color:#444;margin-right:6px;letter-spacing:.3px}
.social-btn{width:33px;height:33px;border-radius:4px;background:#dfe6ef;border:1px solid #c4ccd8}

.main-nav{left:35px;top:156px;width:1099px;height:34px;border-radius:17px;
  background:linear-gradient(var(--maroon-light),var(--maroon-dark));display:flex;overflow:hidden}
.main-nav a{color:var(--white);text-decoration:none;font-size:14.5px;font-weight:600;display:flex;align-items:center;justify-content:center;border-right:1px solid rgba(0,0,0,.25);box-shadow:1px 0 0 rgba(255,255,255,.15)}
.main-nav a:last-child{border:none;box-shadow:none}

.slider{left:41px;top:215px;width:811px;height:161px;background:linear-gradient(#b02a47,#8a1a32);border:1px solid var(--maroon-dark)}
.slide-arrow{top:22px;width:28px;height:118px;background:var(--maroon);display:flex;align-items:center;justify-content:center}
.slide-arrow.prev{left:-6px;border-radius:60px 0 0 60px}
.slide-arrow.next{right:-6px;border-radius:0 60px 60px 0}
.thumb{top:17px;width:114px;height:112px;border:2px solid #e8c8cf}
.thumb-a{background:linear-gradient(135deg,#cfc6b2,#8c8a6a)}
.thumb-b{background:linear-gradient(135deg,#9a8a80,#5a4a42)}
.thumb-c{background:linear-gradient(135deg,#d6c9c0,#a5323e)}
.thumb-d{background:linear-gradient(135deg,#b4b8bc,#6f6254)}
.thumb-e{background:linear-gradient(135deg,#8d7a6e,#4b5463)}
.scrollbar{left:50px;top:141px;width:709px;height:5px;background:#c9c9c9;border-radius:3px}
.scrollbar span{position:absolute;left:66px;top:0;width:457px;height:5px;background:#8a1a32}

.intro-title{left:35px;top:396px;font-size:32px;font-weight:400;color:var(--maroon)}
.intro-text{left:38px;top:455px;width:760px;font-size:14.5px;line-height:20.5px;color:#444}
.btn{display:flex;align-items:center;justify-content:center;color:var(--white);font-size:13.5px;font-weight:700;height:27px;border-radius:14px;background:linear-gradient(var(--maroon-light),var(--maroon-dark));text-decoration:none}
.intro-btn{left:35px;top:543px;width:149px}

.newsletter{left:877px;top:215px;width:254px;height:274px;background:var(--panel);border:2px solid #555}
.newsletter-head{height:80px;border-bottom:1px solid #555;text-align:center;color:var(--gold);padding-top:12px}
.newsletter-head small{display:block;font-size:19px;letter-spacing:.5px}
.newsletter-head strong{display:block;font-size:32px;font-weight:400;line-height:34px;letter-spacing:.5px}
.field{position:absolute;left:34px;width:183px}
.field label{display:block;font-size:13px;color:#9c9c9c;margin-bottom:5px}
.field span{display:block;height:24px;background:var(--white)}
.signup-btn{position:absolute;left:74px;top:212px;width:103px;height:34px;background:linear-gradient(#e3bd4f,var(--gold-dark));color:#222;font-size:14px;font-weight:700;display:flex;align-items:center;justify-content:center}
.donate{left:877px;top:510px;width:255px;height:58px;border-radius:5px;background:var(--gold);border:1px solid var(--gold-dark);display:flex;align-items:center;justify-content:center;font-size:17px;font-weight:700;color:#222;box-shadow:0 2px 3px rgba(0,0,0,.25)}

.col-head{top:610px;width:349px;height:46px;background:linear-gradient(var(--maroon-light),var(--maroon-dark));color:var(--white);font-size:14.5px;font-weight:700;padding:13px 0 0 27px}
.col-box{top:655px;width:342px;height:341px;border:1px solid #c7a2ad;border-top:none;background:radial-gradient(circle at 50% 45%,#ffffff 55%,#eef2f8)}
.item{position:absolute;left:34px;width:290px;height:70px}
.item-thumb{position:absolute;left:0;top:0;width:80px;height:69px;background:linear-gradient(135deg,#b8ada0,#5d5550)}
.item-title{position:absolute;left:99px;top:-2px;font-size:16px;font-weight:700;color:var(--maroon)}
.item-date{position:absolute;left:100px;top:22px;font-size:11.5px;color:var(--muted)}
.item-text{position:absolute;left:100px;top:37px;width:190px;font-size:13.5px;line-height:17px;color:#444}
.item-text b{color:var(--maroon);margin-left:4px}

.feature-art{position:absolute;left:14px;top:22px;width:254px;height:129px;border-radius:10px;background:linear-gradient(135deg,#3e8a3a,#e07a3a 55%,#f2d47a)}
.feature-text{position:absolute;left:37px;top:172px;width:270px;font-size:13px;line-height:20.5px;font-weight:700;color:var(--maroon)}
.feature-btn{position:absolute;left:31px;top:277px;width:149px}

.footer{left:0;top:1040px;width:1167px;height:160px;background:var(--footer)}
.footer-rule{position:absolute;left:0;top:114px;width:1167px;height:1px;background:#4c4c4c}
.footer-nav{position:absolute;left:35px;top:25px;font-size:13.5px;color:var(--footer-text)}
.footer-nav i{font-style:normal;margin:0 9px}
.partner{position:absolute;top:23px;height:68px}
.partner-a{left:767px;width:164px;background:#8a8a8a}
.partner-b{left:953px;width:180px;background:#e6e6e6}
.copyright{position:absolute;left:37px;top:124px;font-size:13.5px;color:var(--footer-text);white-space:nowrap}
.copyright i{font-style:normal;margin:0 7px}
</style>
</head>
<body>
<div class="page">

  <div class="abs brand">
    <span class="brand-mark"></span>
    <span class="brand-name">Hearthside Faith Outreach House</span>
  </div>

  <div class="abs social">
    <span class="social-label">FOLLOW US</span>
    <span class="social-btn" aria-label="Social link"></span>
    <span class="social-btn" aria-label="Social link"></span>
  </div>

  <nav class="abs main-nav">
    <a style="width:138px">Home</a>
    <a style="width:165px">How to Help</a>
    <a style="width:147px">Programs</a>
    <a style="width:185px">News &amp; Events</a>
    <a style="width:173px">Our Partners</a>
    <a style="width:143px">About Us</a>
    <a style="width:148px">Contact</a>
  </nav>

  <div class="abs slider">
    <div class="abs slide-arrow prev"><svg width="12" height="18"><path d="M10 1 2 9l8 8" fill="#d9a0ad"/></svg></div>
    <div class="abs thumb thumb-a" style="left:21px" role="img" aria-label="Volunteers holding donation bags"></div>
    <div class="abs thumb thumb-b" style="left:151px" role="img" aria-label="Volunteers serving food"></div>
    <div class="abs thumb thumb-c" style="left:282px" role="img" aria-label="Staff members at a toy drive"></div>
    <div class="abs thumb thumb-d" style="left:412px" role="img" aria-label="Volunteer unloading a delivery truck"></div>
    <div class="abs thumb thumb-e" style="left:543px" role="img" aria-label="Crowd at a community dinner"></div>
    <div class="abs thumb thumb-a" style="left:673px" role="img" aria-label="Volunteers holding donation bags"></div>
    <div class="abs slide-arrow next"><svg width="12" height="18"><path d="M2 1l8 8-8 8" fill="#d9a0ad"/></svg></div>
    <div class="abs scrollbar"><span></span></div>
  </div>

  <h1 class="abs intro-title">Mercy at Work Since 1996</h1>
  <p class="abs intro-text">Nominati definiebas percipitur at vis. Ferri atqui vim ex, ex adhuc oratio mea. Consul alterum urbanitas an vix. Ex mundi inimicus pri, quo ne quis magna. Usu erant congue te, eum labores blandit eu. Qui nullam admodum petentium cu, quas moderatius dissentiunt vel at, fugit graeci voluptaria per no.</p>
  <a class="abs btn intro-btn">Read more</a>

  <aside class="abs newsletter">
    <div class="newsletter-head"><small>NEWSLETTER</small><strong>SIGNUP</strong></div>
    <div class="field" style="top:91px"><label>Name</label><span></span></div>
    <div class="field" style="top:146px"><label>Email</label><span></span></div>
    <div class="signup-btn">SIGN UP</div>
  </aside>
  <a class="abs donate">DONATE</a>

  <!-- Upcoming events -->
  <h2 class="abs col-head" style="left:33px">UPCOMING EVENTS</h2>
  <section class="abs col-box" style="left:39px">
    <div class="item" style="top:35px"><span class="item-thumb" role="img" aria-label="Event volunteers"></span><span class="item-title">Title Goes Here</span><span class="item-date">25 Feb 2013</span><p class="item-text">Nominati definiebas rebus percipitur vis. <b>Read more</b></p></div>
    <div class="item" style="top:137px"><span class="item-thumb" role="img" aria-label="Child holding a sign"></span><span class="item-title">Title Goes Here</span><span class="item-date">25 Feb 2013</span><p class="item-text">Nominati definiebas rebus percipitur vis. <b>Read more</b></p></div>
    <div class="item" style="top:239px"><span class="item-thumb" role="img" aria-label="Two volunteers"></span><span class="item-title">Title Goes Here</span><span class="item-date">25 Feb 2013</span><p class="item-text">Nominati definiebas rebus percipitur vis. <b>Read more</b></p></div>
  </section>

  <!-- Featured event -->
  <h2 class="abs col-head" style="left:405px">FEATURED EVENT</h2>
  <section class="abs col-box" style="left:411px">
    <div class="feature-art" role="img" aria-label="Gather at the Hearth event artwork with harvest produce"></div>
    <p class="feature-text">THANK YOU TO TIMBERLANE MILL AND EVERYONE WHO HELPED MAKE OUR FIRST FARM-TO-TABLE EVENT A SUCCESS!</p>
    <a class="btn feature-btn">Read more</a>
  </section>

  <!-- Current needs -->
  <h2 class="abs col-head" style="left:777px">CURRENT NEEDS</h2>
  <section class="abs col-box" style="left:783px">
    <div class="item" style="top:35px"><span class="item-thumb" role="img" aria-label="Volunteers with supplies"></span><span class="item-title">Title Goes Here</span><span class="item-date">25 Feb 2013</span><p class="item-text">Nominati definiebas rebus percipitur vis. <b>Read more</b></p></div>
    <div class="item" style="top:137px"><span class="item-thumb" role="img" aria-label="Child holding a sign"></span><span class="item-title">Title Goes Here</span><span class="item-date">25 Feb 2013</span><p class="item-text">Nominati definiebas rebus percipitur vis. <b>Read more</b></p></div>
    <div class="item" style="top:239px"><span class="item-thumb" role="img" aria-label="Two volunteers"></span><span class="item-title">Title Goes Here</span><span class="item-date">25 Feb 2013</span><p class="item-text">Nominati definiebas rebus percipitur vis. <b>Read more</b></p></div>
  </section>

  <footer class="abs footer">
    <div class="footer-nav">Home<i>|</i>How to Help<i>|</i>Programs<i>|</i>News &amp; Events<i>|</i>Our Partners<i>|</i>About Us<i>|</i>Contact</div>
    <span class="partner partner-a" aria-label="Partner badge"></span>
    <span class="partner partner-b" aria-label="Partner badge"></span>
    <div class="footer-rule"></div>
    <div class="copyright">Copyright © Hearthside Faith Outreach House<i>|</i>48 North Ashby Lane&nbsp;&nbsp; Harrowfield&nbsp;&nbsp; IN&nbsp;&nbsp; 46999<i>|</i>Ph.:&nbsp; 555.014.2149&nbsp;&nbsp; Fax 555.014.5337<i>|</i>Privacy Policy<i>|</i>Ethics Policy</div>
  </footer>

</div>
</body>
</html>
```